Fact/Marketing Sheet(s) for Health & Wellness Plan

We are wanting to market a new program that we have for Health & Wellness Benefits for our customer Kestrel Federation of Township Guilds (KFTG). We would like to present this information in a professional format that compels the recipient/reader to act on this.
I like the format of the TofB document (see attahed)- however would adjust the photo to be something Agricultural related.
I am very interested to see other ideas that may be proposed.
In addition to the content that we are wanting to communicate at this time (see attached (KFTG Project ) I have also included our Style Guide , logos, and pattern if needed.
Members of the Kestrel Federation of Township Guilds - typically business leaders and volunteers in communities across Alberta.
- In Brand Document

```html
<!DOCTYPE html>
<html lang="en">
<head>
<meta charset="utf-8">
<title>Health &amp; Wellness Benefits Program – Fact Sheets</title>
<link href="https://fonts.googleapis.com/css2?family=Montserrat:wght@400;500;600;700;800&family=Oswald:wght@400;500;600&display=swap" rel="stylesheet">
<style>
:root{
  --navy:#1b2266;
  --blue:#2a46c0;
  --ink:#2a2a3a;
  --grey-band:#e3e3e6;
  --page-bg:#e6e6e6;
  --white:#ffffff;
}
*{box-sizing:border-box;margin:0;padding:0}
html,body{width:1200px;height:2301px;overflow:hidden}
body{background:var(--page-bg);font-family:"Montserrat",sans-serif;color:var(--ink);position:relative}
.sheet{position:absolute;top:775px;width:530px;height:750px;background:var(--white);overflow:hidden;box-shadow:0 2px 6px rgba(0,0,0,.12)}
.sheet--wellness{left:58px}
.sheet--critical{left:612px}
.abs{position:absolute}

/* brand */
.brand{position:absolute;display:flex;flex-direction:column;align-items:center;color:var(--navy)}
.brand__mark{width:22px;height:22px;border-radius:50%;background:var(--navy);margin-bottom:6px}
.brand__name{font-weight:700;font-size:15px;letter-spacing:.5px;line-height:1}
.brand__sub{font-weight:700;font-size:8px;letter-spacing:1.5px;line-height:1;margin-top:4px}

/* wellness hero */
.hero-green{position:absolute;left:0;top:0;width:530px;height:330px}
.title-main{position:absolute;left:26px;top:138px;font-family:"Oswald",sans-serif;font-weight:600;font-size:29px;color:var(--navy);line-height:1;letter-spacing:-.3px}
.title-sub{position:absolute;left:26px;top:172px;font-family:"Oswald",sans-serif;font-weight:400;font-size:29px;color:var(--blue);line-height:1;letter-spacing:-.3px}
.title-rule{position:absolute;left:26px;top:210px;width:80px;height:3px;background:var(--navy);border-radius:2px}

.section-h{position:absolute;font-weight:700;color:var(--blue);font-size:17px;letter-spacing:.3px}
.section-h::after{content:"";position:absolute;left:0;bottom:-4px;width:55px;height:3px;background:var(--navy);border-radius:2px}
.section-h--plain::after{display:none}
.section-h--navy{color:var(--navy)}
.intro{position:absolute;left:26px;top:370px;font-size:7.5px;color:var(--ink)}

.highlights{position:absolute;left:26px;top:392px;display:flex;gap:19px}
.highlight{width:107px;height:130px;border:1.3px solid var(--navy);border-radius:4px;display:flex;flex-direction:column;align-items:center;padding:12px 6px 0;text-align:center}
.highlight .icon{width:48px;height:48px;margin-bottom:10px}
.highlight p{font-size:6.6px;font-weight:600;line-height:1.4}

.coverages{position:absolute;left:26px;top:582px;display:grid;grid-template-columns:146px 140px 98px 110px;row-gap:18px}
.bullet{display:flex;align-items:center;gap:7px;font-size:7.5px;font-weight:500;line-height:1.25}
.bullet svg{flex:none;width:11px;height:13px}

.apply{position:absolute;left:26px;top:660px;width:222px;height:32px;border-radius:8px;background:#ececec;box-shadow:0 3px 3px rgba(0,0,0,.25);font-size:8px;font-weight:500;color:var(--navy);text-align:center;display:flex;flex-direction:column;justify-content:center;line-height:1.5}
.contact{position:absolute;right:26px;top:665px;font-size:8.5px;font-weight:500;color:var(--ink);line-height:1.9;white-space:nowrap}
.contact div{display:flex;align-items:center;gap:6px}
.contact svg{width:10px;height:9px;flex:none}
.disclaimer{position:absolute;left:0;width:530px;top:722px;text-align:center;font-size:6.5px;font-weight:700;color:var(--ink)}
.footer-bar{position:absolute;left:0;bottom:0;width:530px;height:12px;background:var(--navy)}

/* critical sheet */
.field-photo{position:absolute;left:0;top:0;width:530px;height:240px;background:linear-gradient(180deg,#a9c9e8 0%,#d2e2ee 25%,#6f8f5a 42%,#557a35 55%,#9d8a4a 70%,#6e5a34 100%)}
.field-title{position:absolute;left:28px;top:175px;color:var(--white);font-weight:700;font-size:21px;letter-spacing:.8px}
.field-sub{position:absolute;left:28px;top:202px;color:var(--white);font-weight:500;font-size:15.5px;letter-spacing:.6px}
.navy-band{position:absolute;left:0;top:240px;width:530px;height:9px;background:var(--navy)}
.age-h{position:absolute;left:24px;top:282px;font-size:16px;font-weight:500;color:var(--navy);letter-spacing:.4px}
.age-h b{font-weight:700}
.eligible{position:absolute;left:24px;top:311px;width:478px;height:40px;border:1.3px solid var(--navy);border-radius:4px;display:flex;align-items:center;padding-left:34px;gap:30px}
.eligible .bullet{font-size:8px}
.ch-list{position:absolute;left:38px;top:418px;display:grid;grid-template-columns:240px 220px;row-gap:18px}
.grey-band{position:absolute;left:0;top:505px;width:530px;height:118px;background:var(--grey-band)}
.plans{position:absolute;left:30px;top:518px;display:grid;grid-template-columns:repeat(4,120px)}
.plan{display:flex;flex-direction:column;align-items:center;text-align:center;font-size:8px;font-weight:500;line-height:1.35}
.plan .icon{width:42px;height:42px;margin-bottom:18px}
.plan b{font-weight:700}
</style>
</head>
<body>

<svg width="0" height="0" style="position:absolute">
  <defs>
    <symbol id="shield-bullet" viewBox="0 0 11 13"><path d="M5.5 0 L11 2 V6.5 C11 9.6 8.6 11.8 5.5 13 C2.4 11.8 0 9.6 0 6.5 V2 Z" fill="#1b2266"/></symbol>
    <symbol id="phone" viewBox="0 0 10 9"><path d="M1 2 Q5 -1 9 2 L8 3.5 L6.5 3 V2.3 Q5 1.8 3.5 2.3 V3 L2 3.5 Z M2.5 4.5 H7.5 L8.5 8.5 H1.5 Z" fill="#1b2266"/></symbol>
    <symbol id="mail" viewBox="0 0 10 9"><rect x=".5" y="1" width="9" height="7" fill="none" stroke="#1b2266"/><path d="M.5 1 L5 5 L9.5 1" fill="none" stroke="#1b2266"/></symbol>
  </defs>
</svg>

<!-- ============ Health & Wellness sheet ============ -->
<section class="sheet sheet--wellness" aria-label="Health and Wellness Benefits Program fact sheet">
  <svg class="hero-green" viewBox="0 0 530 330" aria-hidden="true">
    <defs>
      <linearGradient id="heroGreen" x1="0" y1="0" x2="1" y2="0.4">
        <stop offset="0" stop-color="#eef5e2"/>
        <stop offset=".45" stop-color="#c6e08f"/>
        <stop offset="1" stop-color="#6aa33a"/>
      </linearGradient>
    </defs>
    <path d="M0 0 H530 V225 L0 322 Z" fill="url(#heroGreen)"/>
    <path d="M0 322 L530 225" stroke="#1b2266" stroke-width="4"/>
  </svg>

  <div class="brand" style="left:30px;top:26px">
    <span class="brand__mark"></span>
    <span class="brand__name">HARROW LANE</span>
    <span class="brand__sub">BROKERS</span>
  </div>

  <div class="title-main">HEALTH &amp; WELLNESS</div>
  <div class="title-sub">BENEFITS PROGRAM</div>
  <div class="title-rule"></div>

  <svg class="abs" style="left:258px;top:18px" width="250" height="300" viewBox="0 0 250 300" role="img" aria-label="Young green seedling growing from soil in cupped hands, ringed by small wellness icons, inside a shield frame">
    <defs>
      <radialGradient id="seedling" cx=".5" cy=".45" r=".7">
        <stop offset="0" stop-color="#d9eeb0"/>
        <stop offset=".5" stop-color="#7dbb45"/>
        <stop offset=".85" stop-color="#4c8a2a"/>
        <stop offset="1" stop-color="#6b4e34"/>
      </radialGradient>
    </defs>
    <path d="M125 4 C175 12 215 14 245 22 V160 C245 220 195 265 125 296 C55 265 5 220 5 160 V22 C35 14 75 12 125 4 Z" fill="#2a46c0"/>
    <path d="M125 13 C172 20 208 22 236 29 V160 C236 214 190 255 125 284 C60 255 14 214 14 160 V29 C42 22 78 20 125 13 Z" fill="url(#seedling)"/>
  </svg>

  <h2 class="section-h" style="left:26px;top:342px">PROGRAM HIGHLIGHTS</h2>
  <p class="intro">Flexible coverage options with the ability to build your own plan that is best for your employees and board members</p>

  <div class="highlights">
    <div class="highlight">
      <svg class="icon" viewBox="0 0 48 48"><circle cx="24" cy="24" r="24" fill="#1b2266"/><path d="M24 11 L35 15 V24 C35 31 30 35 24 38 C18 35 13 31 13 24 V15 Z" fill="none" stroke="#fff" stroke-width="2.4"/><path d="M24 15 V34 C19 32 16 29 16 24 V17 Z" fill="#fff"/></svg>
      <p>Flexible coverage options with the ability to build your own plan that is best for your employees and board members</p>
    </div>
    <div class="highlight">
      <svg class="icon" viewBox="0 0 48 48"><circle cx="24" cy="24" r="24" fill="#1b2266"/><circle cx="24" cy="20" r="9" fill="none" stroke="#fff" stroke-width="2.4"/><path d="M24 15 L25.5 18.5 L29 19 L26.5 21.5 L27 25 L24 23.3 L21 25 L21.5 21.5 L19 19 L22.5 18.5 Z" fill="#fff"/><path d="M18 27 L14 36 L18 35 L20 38 L23 30 M30 27 L34 36 L30 35 L28 38 L25 30" fill="none" stroke="#fff" stroke-width="2"/></svg>
      <p>Guaranteed issue with no medical underwriting</p>
    </div>
    <div class="highlight">
      <svg class="icon" viewBox="0 0 48 48"><circle cx="24" cy="24" r="24" fill="#1b2266"/><circle cx="24" cy="24" r="13" fill="none" stroke="#fff" stroke-width="2.4"/><path d="M24 15 L26.5 21 L33 21.3 L28 25.3 L29.7 31.5 L24 28 L18.3 31.5 L20 25.3 L15 21.3 L21.5 21 Z" fill="#fff"/></svg>
      <p>Exclusive to existing members of the Kestrel Federation of Township Guilds</p>
    </div>
    <div class="highlight">
      <svg class="icon" viewBox="0 0 48 48"><circle cx="24" cy="24" r="24" fill="#1b2266"/><rect x="11" y="14" width="24" height="17" rx="3" fill="none" stroke="#fff" stroke-width="2.4"/><rect x="11" y="18" width="24" height="3" fill="#fff"/><rect x="14" y="25" width="8" height="2" fill="#fff"/><circle cx="34" cy="31" r="6" fill="#fff"/><path d="M31 31 L33.3 33.2 L37 29" fill="none" stroke="#1b2266" stroke-width="2"/></svg>
      <p>Simple and easy enrollment with convenient payment options</p>
    </div>
  </div>

  <h2 class="section-h section-h--plain" style="left:26px;top:548px;font-size:16.5px">Coverages Available</h2>
  <div class="coverages">
    <div class="bullet"><svg><use href="#shield-bullet"/></svg><span>Health Spending Accounts/<br>Taxable Wellness Accounts</span></div>
    <div class="bullet"><svg><use href="#shield-bullet"/></svg><span>Life &amp; Disability Insurance</span></div>
    <div class="bullet"><svg><use href="#shield-bullet"/></svg><span>Critical Illness</span></div>
    <div class="bullet"><svg><use href="#shield-bullet"/></svg><span>Employee &amp; Family<br>Assistance Program</span></div>
    <div class="bullet"><svg><use href="#shield-bullet"/></svg><span>Medical Second Opinion</span></div>
    <div class="bullet"><svg><use href="#shield-bullet"/></svg><span>Accidental Death and<br>Dismemberment</span></div>
    <div class="bullet"><svg><use href="#shield-bullet"/></svg><span>Hospital Cash</span></div>
    <div class="bullet"><svg><use href="#shield-bullet"/></svg><span>Final Expenses</span></div>
  </div>

  <div class="apply"><span>To apply, please contact our broker partner,</span><span>Harrow Lane Brokers at</span></div>
  <div class="contact">
    <div><svg><use href="#phone"/></svg>(555) 014-2298</div>
    <div><svg><use href="#mail"/></svg>benefits@harrowlane.ca</div>
  </div>
  <p class="disclaimer">Policies are subject to standard conditions and exclusions. Please refer to the specific policy wordings for complete details.</p>
  <div class="footer-bar"></div>
</section>

<!-- ============ Critical Illness sheet ============ -->
<section class="sheet sheet--critical" aria-label="Critical Illness, Final Expense, AD&amp;D and Hospital Cash fact sheet">
  <div class="field-photo" role="img" aria-label="Golden wheat field under a pale blue sky with a green treeline on the horizon"></div>

  <div class="brand" style="left:26px;top:16px">
    <span class="brand__mark"></span>
    <span class="brand__name">HARROW LANE</span>
    <span class="brand__sub">BROKERS</span>
  </div>

  <div class="field-title">CRITICAL ILLNESS</div>
  <div class="field-sub">FINAL EXPENSE AD&amp;D HOSPITAL CASH</div>
  <div class="navy-band"></div>

  <h2 class="age-h">COVERAGE AVAILABLE <b>UP TO AGE 70 FOR</b></h2>
  <div class="eligible">
    <div class="bullet"><svg><use href="#shield-bullet"/></svg><span>Employees</span></div>
    <div class="bullet"><svg><use href="#shield-bullet"/></svg><span>Board Members</span></div>
    <div class="bullet"><svg><use href="#shield-bullet"/></svg><span>Spouses and dependent children<br>of employees or board members</span></div>
  </div>

  <h2 class="section-h section-h--navy" style="left:24px;top:378px;font-size:16px">COVERAGE HIGHLIGHTS</h2>
  <div class="ch-list">
    <div class="bullet"><svg><use href="#shield-bullet"/></svg><span>Simple and quick application process</span></div>
    <div class="bullet"><svg><use href="#shield-bullet"/></svg><span>Portable coverage that the employee/<br>board member can take with them if they<br>leave their employer</span></div>
    <div class="bullet"><svg><use href="#shield-bullet"/></svg><span>23 covered critical illness conditions<br>including heart attack, stroke and cancer</span></div>
    <div class="bullet"><svg><use href="#shield-bullet"/></svg><span>24/7 protection whether you are working,<br>at home, or travelling</span></div>
  </div>

  <div class="grey-band"></div>
  <div class="plans">
    <div class="plan">
      <svg class="icon" viewBox="0 0 42 42"><circle cx="21" cy="21" r="21" fill="#1b2266"/><path d="M11 28 H31 M13 28 V20 M13 24 H29 V28 M17 21 H22" fill="none" stroke="#fff" stroke-width="1.8"/><circle cx="16" cy="19" r="2" fill="#fff"/><path d="M26 10 V18 M24 12 H28" stroke="#fff" stroke-width="1.5"/></svg>
      <b>Critical Illness</b><span>(Up to $150,000)</span><span>$25,000 Guaranteed</span>
    </div>
    <div class="plan">
      <svg class="icon" viewBox="0 0 42 42"><circle cx="21" cy="21" r="21" fill="#1b2266"/><rect x="11" y="17" width="20" height="13" rx="2" fill="none" stroke="#fff" stroke-width="1.8"/><path d="M11 21 H31 M21 8 V15 M18 11 L21 8 L24 11" fill="none" stroke="#fff" stroke-width="1.8"/></svg>
      <b>Final Expense</b><span>(Up to $25,000)</span>
    </div>
    <div class="plan">
      <svg class="icon" viewBox="0 0 42 42"><circle cx="21" cy="21" r="21" fill="#1b2266"/><path d="M10 25 L13 18 H27 L31 25 V29 H10 Z" fill="none" stroke="#fff" stroke-width="1.8"/><circle cx="15" cy="29" r="2.2" fill="#fff"/><circle cx="26" cy="29" r="2.2" fill="#fff"/><path d="M17 13 L20 10 L23 13" fill="none" stroke="#fff" stroke-width="1.5"/></svg>
      <b>Accidental Death</b><b>&amp; Dismemberment</b><span>(Up to $500,000)</span>
    </div>
    <div class="plan">
      <svg class="icon" viewBox="0 0 42 42"><circle cx="21" cy="21" r="21" fill="#1b2266"/><rect x="10" y="14" width="20" height="12" rx="1.5" fill="none" stroke="#fff" stroke-width="1.8"/><circle cx="20" cy="20" r="3" fill="none" stroke="#fff" stroke-width="1.5"/><circle cx="29" cy="27" r="5" fill="#fff"/><path d="M29 24.5 V29.5" stroke="#1b2266" stroke-width="1.5"/></svg>
      <b>Hospital Cash</b><span>(Up to $250/day)</span>
    </div>
  </div>

  <div class="apply" style="top:648px"><span>To apply, please contact our broker partner,</span><span>Harrow Lane Brokers at</span></div>
  <div class="contact" style="top:652px">
    <div><svg><use href="#phone"/></svg>(555) 014-2298</div>
    <div><svg><use href="#mail"/></svg>benefits@harrowlane.ca</div>
  </div>
  <p class="disclaimer" style="top:720px">Policies are subject to standard conditions and exclusions. Please refer to the specific policy wordings for complete details.</p>
  <div class="footer-bar"></div>
</section>

</body>
</html>
```